Fitness Equipment & Service

I want to make the card eye catching and fun. We are called Corvane Motion Limited and we are based in Wales. We sell, install and service all types of fitness equipment from Skipping ropes, right through the Dumbbells, Kettle bells and Barbells through to state of the art Treadmills, Running Machines and Strength Equipment. We also design and install changing room furniture and lockers.

TYPOGRAPHY
We would like to use Futrura. Futura has an appearance of efficiency and forwardness. The typeface is derived
from simple geometric forms (near-perfect circles, triangles and squares) and is based on strokes of
near-even weight, which are low in contrast. This is most visible in the almost perfectly round stroke of
the o, which is nonetheless slightly ovoid.
The lowercase has tall ascenders, which rise above the cap line. The uppercase
characters present proportions similar to those of classical Roman capitals.

TYPOGRAPHIC CONSIDERATIONS
No Strike though
No Horizontal Scaling
No Drop Shadows
No Effects
Never use less than 120% Leading

OUR CORPORATE COLOURS
BRAND GUIDELINES
We were thinking that our primary colour palette consists of the Acid Green (Pantone 382) and Process Black.

We work closely with tolbrook Ltd and would like to include their name on the card somewhere. I have attached images of the other brands that we work with as an idea or the small icons I have included that illustrate what we do?. I have very kindly been given permission to use any of the images off the files that I have included below, so I hope these help. I will include these below. I would be open to suggestions if it made the card more striking Can you do it?
Updates

Hi All, Just wanted to add a few thoughts but you are the guys with the creative visions (thats why are here) We are based in Wales, UK and we would be open to lots of different ideas on a theme but must be eye catching, Bold and FUN. If you can or think that the Welsh or any dragon could be put in there then go for it (its not a must have) We have also added some ideas for colour but again its over to you!! GO FOR IT ! Thanks and look forward to your visions! Owen

Hi All, Just thought I would sen through the contact details that need to be on the card. (if you want to play around with icons instead of the wording twitter, Facebook, go for it): Corvane Motion Limited Owen Pritchard Managing Director Mob: +44 (0)7382 519 046 e-mail: sales@corvanemotion.co.uk Web: Corvanemotion.co.uk twitter: @motionPostbag Facebook: Corvane Motion Limited

Industry/Entity Type

Fitness

```html
<!DOCTYPE html>
<html lang="en">
<head>
<meta charset="utf-8">
<title>Corvane Motion Limited – Business Card</title>
<link rel="stylesheet" href="https://fonts.googleapis.com/css2?family=Open+Sans:wght@400;700&display=swap">
<style>
  :root {
    --page: #e9eaec;
    --card: #f7f8f9;
    --card-edge: #c9ccd1;
    --acid-green: #c4d600;
    --black: #111111;
    --black-soft: #2a2a2a;
    --ink: #1a1a1a;
    --grey: #555a60;
    --white: #ffffff;
  }
  * { margin: 0; padding: 0; box-sizing: border-box; }
  html, body {
    width: 1200px; height: 970px; overflow: hidden;
    background: var(--page);
    font-family: "Open Sans", Arial, sans-serif;
  }
  .card {
    position: absolute; left: 100px; top: 207px;
    width: 1000px; height: 556px;
    background: var(--card);
    border: 1px solid var(--card-edge);
  }
  .edge-bar {
    position: absolute; left: 0; top: 113px;
    width: 37px; height: 328px;
    background: var(--acid-green);
  }
  .brand-mark {
    position: absolute; left: 174px; top: 105px;
    width: 234px; height: 234px; border-radius: 50%;
    background: var(--acid-green);
  }
  .brand-name {
    position: absolute; left: 61px; top: 368px; width: 460px;
    text-align: center; white-space: nowrap;
    font-size: 30px; font-weight: 700; line-height: 1.25;
    color: var(--ink);
  }
  .partner-note {
    position: absolute; left: 61px; top: 412px; width: 460px;
    text-align: center; white-space: nowrap;
    font-size: 17px; font-weight: 400; line-height: 1.3;
    color: var(--grey);
  }
  .panel {
    position: absolute; left: 547px; width: 453px;
    background: linear-gradient(90deg, var(--black), var(--black-soft));
    border-left: 6px solid var(--acid-green);
    color: var(--white);
    padding-left: 18px;
  }
  .panel--name { top: 110px; height: 88px; padding-top: 9px; }
  .panel--contact { top: 220px; height: 113px; padding-top: 10px; }
  .panel--social { top: 355px; height: 87px; padding-top: 10px; }
  .person-name { font-size: 31px; font-weight: 700; line-height: 1.25; letter-spacing: 0.5px; color: var(--acid-green); }
  .person-role { font-size: 21px; line-height: 1.25; }
  .line {
    display: flex; align-items: center; gap: 12px;
    font-size: 22px; line-height: 1.4; white-space: nowrap;
  }
  .line svg { width: 20px; height: 20px; flex: none; }
  .dot { width: 14px; height: 14px; border-radius: 50%; background: var(--acid-green); margin: 0 3px; flex: none; }
</style>
</head>
<body>
  <div class="card">
    <div class="edge-bar"></div>
    <div class="brand-mark"></div>
    <div class="brand-name">Corvane Motion Limited</div>
    <div class="partner-note">In partnership with tolbrook Ltd</div>

    <div class="panel panel--name">
      <div class="person-name">OWEN PRITCHARD</div>
      <div class="person-role">Managing Director</div>
    </div>

    <div class="panel panel--contact">
      <div class="line">
        <svg viewBox="0 0 20 20"><rect x="6" y="2" width="8" height="16" rx="1.5" fill="none" stroke="#c4d600" stroke-width="1.6"/><circle cx="10" cy="15" r="1" fill="#c4d600"/></svg>
        +44 (0)7382 519 046
      </div>
      <div class="line">
        <svg viewBox="0 0 20 20"><rect x="2" y="5" width="16" height="11" fill="#c4d600"/><path d="M2 5 L10 11 L18 5" fill="none" stroke="#111111" stroke-width="1.4"/></svg>
        sales@corvanemotion.co.uk
      </div>
      <div class="line">
        <svg viewBox="0 0 20 20"><rect x="2.5" y="4" width="15" height="10" fill="none" stroke="#c4d600" stroke-width="1.6"/><rect x="7" y="15" width="6" height="1.8" fill="#c4d600"/></svg>
        Corvanemotion.co.uk
      </div>
    </div>

    <div class="panel panel--social">
      <div class="line"><span class="dot"></span>@motionPostbag</div>
      <div class="line"><span class="dot"></span>Corvane Motion Limited</div>
    </div>
  </div>
</body>
</html>
```